Reclaimed Tavern & Inn Kit need a website

We need a website designed and created to facilitate us to promote & sell our products online. We buy excess / clearance lots of pub, cafe, restaurant & hotel furniture and equipment (usually from businesses that have excess inventory after a refurb or have closed down). We then sell these to other businesses mainly through our Facebook page "Reclaimed Tavern & Inn Kit" but the process is cumbersome for the following reasons:
1) We dont have a stock list and images as it changes daily and people can only rely on recent posts and dont know if something is for sale still or is sold
2) we do not have the facility to sell online.

We are open to ideas and design concepts

We already have a logo & stationery deisgned

its probably best to look through our Facebook page to better understand what we do

We would consider a catalogue / by department / category user interface such as:
https://rehomed-taproom-gear.co.uk/

Our preference would be to change / delete / update stock via smartphone to best facilitate the maintenance of the website which i will do myself

Suggested categories would include:
Bar Furniture
Bar Equipment
Restaurant Furniture
Catering Equipment
Bedroom Furniture
Miscellaneous

Sub categories would include:
Bar Furniture:
Bar Stools
Bar Tables
Benches
Tub chairs
Arm chairs
Pub Mirrors
Pub Signs
Pub Memorabilia

Bar Equipment:
Bottle Coolers
Ice Machines
Glass Washers
Tills
Lighting
Sound
Wireless waiter
Glassware
Taps
Line coolers
Snooker tables
Pool tables
gaming machines

Restaurant Furniture:
Tables
Chairs
Wine racks
Dressers
Couches
Bench seating
Tub Chairs
Arm chairs
High chairs
Menu boards
Mirrors
Pictures

Catering Equipment:
Fridges
Freezers
Ovens
Cookers
Fryers
Carvery units
Hot display units
Refrigerated displays
Sinks
Stainless steel units
Microwaves
Mixers
Crockery
Cutlery
Utensils
Glassware

Bedroom Furniture:
Beds
Headboards
Wardrobes
Lockers
Dressing Tables
Mirrors
Lamps
Pictures

Profit sharing schemes:
Pool Tables
Juke Boxes
Gaming Machines

Target Market(s)

Pubs
Restaurants
cafes
guest houses
hotels

Industry/Entity Type

Hospitality

Number of Pages Required

5+ page

Colors

Designer to choose colors to be used in the design.

Requirements
Must have
• Website featuring our categories of stock to sell
Nice to have
• Ecommerce option
Should not have
• just a front page

```html
<!DOCTYPE html>
<html lang="en">
<head>
<meta charset="utf-8">
<title>Reclaimed Tavern &amp; Inn Kit</title>
<link rel="stylesheet" href="https://fonts.googleapis.com/css2?family=Montserrat:wght@500;600;700;800&family=Open+Sans:wght@400;600&display=swap">
<style>
:root{
  --red:#a5121c;
  --ink:#222;
  --muted:#555;
  --page:#eeeeee;
  --side:#f7f7f7;
  --line:#dcdcdc;
  --white:#fff;
  --foot:#2d2d2d;
  --foot-deep:#232323;
  --foot-field:#4d4f53;
}
*{box-sizing:border-box;margin:0;padding:0}
html,body{width:1200px;height:2378px;overflow:hidden}
body{position:relative;background:var(--page);font-family:"Open Sans",Arial,sans-serif;color:var(--ink)}
a{color:inherit;text-decoration:none}
.head{position:absolute;left:0;top:0;width:1200px;height:80px;background:var(--white);border-bottom:1px solid var(--line)}
.brand{position:absolute;left:14px;top:24px;display:flex;align-items:center;gap:8px}
.brand-mark{width:22px;height:22px;background:var(--red)}
.brand-name{font-family:"Montserrat",sans-serif;font-weight:700;font-size:13px;color:var(--ink);letter-spacing:.2px;text-transform:uppercase}
.nav{position:absolute;top:29px;left:472px;display:flex;font-family:"Montserrat",sans-serif;font-size:12px;font-weight:500;text-transform:uppercase}
.nav a{position:absolute;white-space:nowrap;line-height:22px}
.nav .on{background:var(--red);color:var(--white);padding:0 9px}
.caret{display:inline-block;width:0;height:0;border-left:5px solid transparent;border-right:5px solid transparent;border-top:6px solid var(--red);margin-left:7px;vertical-align:1px}
.cart{position:absolute;left:997px;top:28px;display:flex;align-items:center;gap:6px;font-size:11px}
.cart-box{border:1px solid var(--line);padding:3px 8px}
.login{position:absolute;left:1089px;top:27px;width:71px;height:27px;border:1px solid var(--red);color:var(--red);font-family:"Montserrat",sans-serif;font-size:12px;font-weight:600;text-align:center;line-height:25px}

.side{position:absolute;left:0;top:81px;width:195px;height:1967px;background:var(--side);border-right:1px solid var(--line)}
.search{height:50px;display:flex;align-items:center;gap:12px;padding-left:15px;font-size:12px;color:var(--muted);border-bottom:1px solid var(--line)}
.side-title{margin-top:2px;height:30px;background:var(--red);color:var(--white);font-family:"Montserrat",sans-serif;font-size:11px;font-weight:700;display:flex;align-items:center;justify-content:space-between;padding:0 14px}
.cat{font-family:"Montserrat",sans-serif;font-size:11px;font-weight:600;height:33px;display:flex;align-items:center;justify-content:space-between;padding:0 14px 0 15px;border-bottom:1px solid var(--line)}
.sub{list-style:none;padding:4px 0 12px 33px;border-bottom:1px solid var(--line)}
.sub li{font-size:11px;color:#333;line-height:20px;position:relative}
.sub li::before{content:"";position:absolute;left:-11px;top:7px;border-left:4px solid #333;border-top:3px solid transparent;border-bottom:3px solid transparent}
.price-head{margin-top:22px;height:34px;display:flex;align-items:center;justify-content:space-between;padding:0 14px;font-family:"Montserrat",sans-serif;font-size:11px;font-weight:700;border-bottom:1px solid var(--line)}
.price-head span b{font-size:15px;margin-right:10px}
.range{display:flex;align-items:center;gap:9px;padding:15px 12px;font-size:10px;color:var(--muted)}
.range span.field{width:71px;height:29px;background:var(--white);border:1px solid var(--line);padding-left:8px;line-height:27px}

.hero{position:absolute;left:222px;top:108px;width:951px;height:336px;background:linear-gradient(100deg,#1a1310 0%,#3b2418 45%,#5a3322 70%,#8a1a22 100%)}
.hero h1{position:absolute;left:57px;top:101px;color:var(--white);font-family:"Montserrat",sans-serif;font-weight:800;font-size:27px;line-height:33px}
.hero .shop{position:absolute;left:60px;top:187px;width:125px;height:36px;background:var(--red);color:var(--white);font-family:"Montserrat",sans-serif;font-size:13px;font-weight:700;text-align:center;line-height:36px}
.dots{position:absolute;left:418px;top:291px;display:flex;gap:15px}
.dots i{width:9px;height:9px;border-radius:50%;background:var(--white)}
.dots i.now{background:var(--red);box-shadow:0 0 0 2px var(--white)}

.list-title{position:absolute;left:222px;top:476px;font-family:"Montserrat",sans-serif;font-size:23px;font-weight:700}
.list-rule{position:absolute;left:223px;top:516px;width:40px;height:3px;background:#aaa}
.find{position:absolute;left:729px;top:480px;width:156px;height:29px;background:var(--white);border:1px solid var(--line);font-size:9px;color:#888;padding-left:10px;line-height:27px}
.find svg{position:absolute;right:9px;top:9px}
.sort{position:absolute;left:905px;top:477px;width:179px;height:35px;background:var(--white);border:1px solid var(--line);font-size:11px;padding-left:14px;line-height:33px}
.sort svg{position:absolute;right:12px;top:13px}
.view-grid{position:absolute;left:1106px;top:481px;width:30px;height:28px;background:var(--red)}
.view-list{position:absolute;left:1148px;top:488px}

.grid{position:absolute;left:223px;top:564px;display:grid;grid-template-columns:repeat(4,222px);column-gap:20px;row-gap:27px}
.card{width:222px;height:315px;background:var(--white);position:relative}
.card .shot{height:171px;position:relative}
.mail{position:absolute;right:7px;top:9px;width:25px;height:25px;border-radius:50%;background:#1d1d1d;border:1px solid #777;display:flex;align-items:center;justify-content:center}
.tag{position:absolute;left:-6px;top:130px;height:32px;padding:0 14px;background:var(--red);color:var(--white);font-family:"Montserrat",sans-serif;font-weight:700;font-size:15px;line-height:32px}
.card h3{font-family:"Montserrat",sans-serif;font-size:11px;font-weight:700;line-height:14px;margin:21px 20px 9px}
.card p{font-size:10px;line-height:13px;color:#333;margin:0 20px;white-space:nowrap}
.more{display:block;margin:17px 20px 0;color:var(--red);font-family:"Montserrat",sans-serif;font-size:10px;font-weight:700}
.more::after{content:"";display:inline-block;width:5px;height:5px;border-right:2px solid var(--red);border-top:2px solid var(--red);transform:rotate(45deg);margin-left:8px;vertical-align:1px}

.show{position:absolute;left:639px;top:1954px;width:117px;height:38px;background:#dedede;border:1px solid #c7c7c7;font-family:"Montserrat",sans-serif;font-size:11px;font-weight:600;text-align:center;line-height:36px;color:#333}

.foot{position:absolute;left:0;top:2048px;width:1200px;height:250px;background:var(--foot);color:var(--white)}
.foot h4{position:absolute;top:60px;font-family:"Montserrat",sans-serif;font-size:12px;font-weight:700;text-transform:uppercase}
.links{position:absolute;left:49px;top:99px;list-style:none;font-size:11px;line-height:16px}
.contact{position:absolute;left:254px;top:87px;list-style:none;font-size:11px;line-height:16px}
.contact li{position:relative;padding-left:21px;margin-bottom:19px}
.contact svg{position:absolute;left:0;top:3px}
.email-field{position:absolute;left:579px;top:101px;width:215px;height:45px;background:var(--foot-field);font-size:11px;padding-left:42px;line-height:45px}
.email-field svg{position:absolute;left:16px;top:18px}
.signup{position:absolute;left:579px;top:162px;width:84px;height:31px;background:var(--red);font-family:"Montserrat",sans-serif;font-size:13px;font-weight:700;text-align:center;line-height:31px}
.foot-brand{position:absolute;left:872px;top:70px;width:301px;text-align:center;padding:10px 0 14px;border-bottom:2px solid var(--red);display:flex;justify-content:center;align-items:center;gap:10px}
.foot-brand .brand-mark{width:24px;height:24px}
.foot-brand .brand-name{color:var(--white);font-size:15px}
.social{position:absolute;left:936px;top:165px;display:flex;gap:24px}
.social i{width:25px;height:25px;border-radius:50%;background:var(--white)}
.base{position:absolute;left:0;top:2298px;width:1200px;height:80px;background:var(--foot-deep);color:#ddd;font-size:11px;text-align:center;line-height:92px}
</style>
</head>
<body>

<header class="head">
  <a class="brand" href="#"><span class="brand-mark"></span><span class="brand-name">Reclaimed Tavern &amp; Inn Kit</span></a>
  <nav class="nav">
    <a class="on" style="left:0">Home</a>
    <a style="left:76px">About Us</a>
    <a style="left:173px">Categories<span class="caret"></span></a>
    <a style="left:295px">Information</a>
    <a style="left:411px">Contact Us</a>
  </nav>
  <div class="cart">
    <svg width="22" height="20" viewBox="0 0 22 20" aria-hidden="true"><path d="M1 3h4l3 10h10l3-7H7" fill="none" stroke="#333" stroke-width="1.6"/><circle cx="9" cy="17" r="1.6" fill="#333"/><circle cx="17" cy="17" r="1.6" fill="#333"/><circle cx="8" cy="3" r="3.5" fill="#d33"/></svg>
    <span class="cart-box">My Cart</span>
  </div>
  <a class="login" href="#">LOGIN</a>
</header>

<aside class="side">
  <div class="search">
    <svg width="13" height="13" viewBox="0 0 13 13" aria-hidden="true"><circle cx="5.5" cy="5.5" r="4.3" fill="none" stroke="#333" stroke-width="1.6"/><path d="M8.6 8.6l3.5 3.5" stroke="#333" stroke-width="1.8"/></svg>
    Search Items
  </div>
  <div class="side-title">CATEGORIES <svg width="12" height="8" viewBox="0 0 12 8"><path d="M1 7l5-5 5 5" fill="none" stroke="#fff" stroke-width="2"/></svg></div>
  <div class="cat">Bar Furniture <svg width="12" height="8" viewBox="0 0 12 8"><path d="M1 7l5-5 5 5" fill="none" stroke="#222" stroke-width="2"/></svg></div>
  <ul class="sub">
    <li>Bar Stools</li><li>Bar Tables</li><li>Benches</li><li>Tub chairs</li><li>Arm chairs</li><li>Pub Mirrors</li><li>Pub Signs</li><li>Pub Memorabilia</li>
  </ul>
  <div class="cat">Bar Equipment <svg width="12" height="8" viewBox="0 0 12 8"><path d="M1 1l5 5 5-5" fill="none" stroke="#222" stroke-width="2"/></svg></div>
  <div class="cat">Restaurant Furniture <svg width="12" height="8" viewBox="0 0 12 8"><path d="M1 1l5 5 5-5" fill="none" stroke="#222" stroke-width="2"/></svg></div>
  <div class="cat">Catering Equipment <svg width="12" height="8" viewBox="0 0 12 8"><path d="M1 1l5 5 5-5" fill="none" stroke="#222" stroke-width="2"/></svg></div>
  <div class="cat">Bedroom Furniture <svg width="12" height="8" viewBox="0 0 12 8"><path d="M1 1l5 5 5-5" fill="none" stroke="#222" stroke-width="2"/></svg></div>
  <div class="cat">Miscellaneous <svg width="12" height="8" viewBox="0 0 12 8"><path d="M1 1l5 5 5-5" fill="none" stroke="#222" stroke-width="2"/></svg></div>
  <div class="price-head"><span><b>$</b>PRICE RANGE</span><svg width="12" height="8" viewBox="0 0 12 8"><path d="M1 7l5-5 5 5" fill="none" stroke="#222" stroke-width="2"/></svg></div>
  <div class="range"><span class="field">$ Min</span>to<span class="field">$ Max</span></div>
</aside>

<section class="hero" role="img" aria-label="Photo of a pub bar counter with beer taps and wooden bar stools">
  <h1>RECLAIMED TAVERN<br>&amp; INN KIT</h1>
  <a class="shop" href="#">SHOP NOW</a>
  <div class="dots"><i></i><i></i><i class="now"></i><i></i><i></i></div>
</section>

<h2 class="list-title">PUB EQUIPMENT</h2>
<div class="list-rule"></div>
<div class="find">SEARCH<svg width="9" height="9" viewBox="0 0 13 13"><circle cx="5.5" cy="5.5" r="4.3" fill="none" stroke="#333" stroke-width="2"/><path d="M8.6 8.6l3.5 3.5" stroke="#333" stroke-width="2"/></svg></div>
<div class="sort">Sort by : Popularity<svg width="11" height="7" viewBox="0 0 12 8"><path d="M1 1l5 5 5-5" fill="none" stroke="#222" stroke-width="2"/></svg></div>
<div class="view-grid"><svg width="30" height="28" viewBox="0 0 30 28"><g fill="#fff"><rect x="9" y="8" width="3" height="3"/><rect x="13.5" y="8" width="3" height="3"/><rect x="18" y="8" width="3" height="3"/><rect x="9" y="12.5" width="3" height="3"/><rect x="13.5" y="12.5" width="3" height="3"/><rect x="18" y="12.5" width="3" height="3"/><rect x="9" y="17" width="3" height="3"/><rect x="13.5" y="17" width="3" height="3"/><rect x="18" y="17" width="3" height="3"/></g></svg></div>
<svg class="view-list" width="18" height="14" viewBox="0 0 18 14"><g fill="#444"><rect x="0" y="0" width="3" height="2"/><rect x="5" y="0" width="13" height="2"/><rect x="0" y="6" width="3" height="2"/><rect x="5" y="6" width="13" height="2"/><rect x="0" y="12" width="3" height="2"/><rect x="5" y="12" width="13" height="2"/></g></svg>

<main class="grid">
  <article class="card"><div class="shot" role="img" aria-label="Stainless steel refrigerated prep counter" style="background:linear-gradient(160deg,#4b4f52,#9aa0a3 60%,#3a3d3f)"><span class="mail"><svg width="11" height="8" viewBox="0 0 11 8"><rect width="11" height="8" rx="1" fill="#fff"/><path d="M0.5 .8l5 3.6 5-3.6" fill="none" stroke="#1d1d1d" stroke-width="1"/></svg></span><span class="tag">£10</span></div><h3>LOREM IPSUM IS SIMPLY DUMMY</h3><p>Contrary to popular belief, Lorem<br>Ipsum is not simply random text.<br>It has roots .</p><a class="more">VIEW DETAIL</a></article>
  <article class="card"><div class="shot" role="img" aria-label="Round dark wooden pub table" style="background:linear-gradient(160deg,#2e2a26,#5a3424 55%,#3a2a22)"><span class="mail"><svg width="11" height="8" viewBox="0 0 11 8"><rect width="11" height="8" rx="1" fill="#fff"/><path d="M0.5 .8l5 3.6 5-3.6" fill="none" stroke="#1d1d1d" stroke-width="1"/></svg></span><span class="tag">£20</span></div><h3>LOREM IPSUM IS SIMPLY DUMMY</h3><p>Contrary to popular belief, Lorem<br>Ipsum is not simply random text.<br>It has roots .</p><a class="more">VIEW DETAIL</a></article>
  <article class="card"><div class="shot" role="img" aria-label="Glass door bottle cooler" style="background:linear-gradient(160deg,#6d7174,#c4c7c8 50%,#55595b)"><span class="mail"><svg width="11" height="8" viewBox="0 0 11 8"><rect width="11" height="8" rx="1" fill="#fff"/><path d="M0.5 .8l5 3.6 5-3.6" fill="none" stroke="#1d1d1d" stroke-width="1"/></svg></span><span class="tag">£25</span></div><h3>LOREM IPSUM IS SIMPLY DUMMY</h3><p>Contrary to popular belief, Lorem<br>Ipsum is not simply random text.<br>It has roots .</p><a class="more">VIEW DETAIL</a></article>
  <article class="card"><div class="shot" role="img" aria-label="Round wooden cafe tables" style="background:linear-gradient(160deg,#3a3634,#b99a74 55%,#2d2a28)"><span class="mail"><svg width="11" height="8" viewBox="0 0 11 8"><rect width="11" height="8" rx="1" fill="#fff"/><path d="M0.5 .8l5 3.6 5-3.6" fill="none" stroke="#1d1d1d" stroke-width="1"/></svg></span><span class="tag">£32</span></div><h3>LOREM IPSUM IS SIMPLY DUMMY</h3><p>Contrary to popular belief, Lorem<br>Ipsum is not simply random text.<br>It has roots .</p><a class="more">VIEW DETAIL</a></article>

  <article class="card"><div class="shot" role="img" aria-label="Wine chiller cabinet" style="background:linear-gradient(160deg,#2a2626,#6a3a2a 55%,#8a8e90)"><span class="mail"><svg width="11" height="8" viewBox="0 0 11 8"><rect width="11" height="8" rx="1" fill="#fff"/><path d="M0.5 .8l5 3.6 5-3.6" fill="none" stroke="#1d1d1d" stroke-width="1"/></svg></span><span class="tag">£10</span></div><h3>LOREM IPSUM IS SIMPLY DUMMY</h3><p>Contrary to popular belief, Lorem<br>Ipsum is not simply random text.<br>It has roots .</p><a class="more">VIEW DETAIL</a></article>
  <article class="card"><div class="shot" role="img" aria-label="Dark wooden panelled furniture" style="background:linear-gradient(160deg,#3b1e12,#5e3019 55%,#2a140c)"><span class="mail"><svg width="11" height="8" viewBox="0 0 11 8"><rect width="11" height="8" rx="1" fill="#fff"/><path d="M0.5 .8l5 3.6 5-3.6" fill="none" stroke="#1d1d1d" stroke-width="1"/></svg></span><span class="tag">£20</span></div><h3>LOREM IPSUM IS SIMPLY DUMMY</h3><p>Contrary to popular belief, Lorem<br>Ipsum is not simply random text.<br>It has roots .</p><a class="more">VIEW DETAIL</a></article>
  <article class="card"><div class="shot" role="img" aria-label="Gold upholstered tub chairs and small table" style="background:linear-gradient(160deg,#2a1c1c,#8b7340 55%,#2a1f1a)"><span class="mail"><svg width="11" height="8" viewBox="0 0 11 8"><rect width="11" height="8" rx="1" fill="#fff"/><path d="M0.5 .8l5 3.6 5-3.6" fill="none" stroke="#1d1d1d" stroke-width="1"/></svg></span><span class="tag">£25</span></div><h3>LOREM IPSUM IS SIMPLY DUMMY</h3><p>Contrary to popular belief, Lorem<br>Ipsum is not simply random text.<br>It has roots .</p><a class="more">VIEW DETAIL</a></article>
  <article class="card"><div class="shot" role="img" aria-label="Striped cane bistro chairs" style="background:linear-gradient(160deg,#4a4a52,#b08a60 55%,#3a4c9a)"><span class="mail"><svg width="11" height="8" viewBox="0 0 11 8"><rect width="11" height="8" rx="1" fill="#fff"/><path d="M0.5 .8l5 3.6 5-3.6" fill="none" stroke="#1d1d1d" stroke-width="1"/></svg></span><span class="tag">£32</span></div><h3>LOREM IPSUM IS SIMPLY DUMMY</h3><p>Contrary to popular belief, Lorem<br>Ipsum is not simply random text.<br>It has roots .</p><a class="more">VIEW DETAIL</a></article>

  <article class="card"><div class="shot" role="img" aria-label="Blue cube stools" style="background:linear-gradient(160deg,#5a4a3a,#2f4fb0 55%,#3a3a3e)"><span class="mail"><svg width="11" height="8" viewBox="0 0 11 8"><rect width="11" height="8" rx="1" fill="#fff"/><path d="M0.5 .8l5 3.6 5-3.6" fill="none" stroke="#1d1d1d" stroke-width="1"/></svg></span><span class="tag">£10</span></div><h3>LOREM IPSUM IS SIMPLY DUMMY</h3><p>Contrary to popular belief, Lorem<br>Ipsum is not simply random text.<br>It has roots .</p><a class="more">VIEW DETAIL</a></article>
  <article class="card"><div class="shot" role="img" aria-label="Black leather armchairs" style="background:linear-gradient(160deg,#3a3030,#1a1a1c 55%,#4a2a2a)"><span class="mail"><svg width="11" height="8" viewBox="0 0 11 8"><rect width="11" height="8" rx="1" fill="#fff"/><path d="M0.5 .8l5 3.6 5-3.6" fill="none" stroke="#1d1d1d" stroke-width="1"/></svg></span><span class="tag">£20</span></div><h3>LOREM IPSUM IS SIMPLY DUMMY</h3><p>Contrary to popular belief, Lorem<br>Ipsum is not simply random text.<br>It has roots .</p><a class="more">VIEW DETAIL</a></article>
  <article class="card"><div class="shot" role="img" aria-label="Round wooden pub table with ornament" style="background:linear-gradient(160deg,#3a4a36,#6a4a30 55%,#2a2a22)"><span class="mail"><svg width="11" height="8" viewBox="0 0 11 8"><rect width="11" height="8" rx="1" fill="#fff"/><path d="M0.5 .8l5 3.6 5-3.6" fill="none" stroke="#1d1d1d" stroke-width="1"/></svg></span><span class="tag">£25</span></div><h3>LOREM IPSUM IS SIMPLY DUMMY</h3><p>Contrary to popular belief, Lorem<br>Ipsum is not simply random text.<br>It has roots .</p><a class="more">VIEW DETAIL</a></article>
  <article class="card"><div class="shot" role="img" aria-label="Pub gaming machine" style="background:linear-gradient(160deg,#6a6a66,#2a2a2a 50%,#b8a830)"><span class="mail"><svg width="11" height="8" viewBox="0 0 11 8"><rect width="11" height="8" rx="1" fill="#fff"/><path d="M0.5 .8l5 3.6 5-3.6" fill="none" stroke="#1d1d1d" stroke-width="1"/></svg></span><span class="tag">£32</span></div><h3>LOREM IPSUM IS SIMPLY DUMMY</h3><p>Contrary to popular belief, Lorem<br>Ipsum is not simply random text.<br>It has roots .</p><a class="more">VIEW DETAIL</a></article>

  <article class="card"><div class="shot" role="img" aria-label="Stainless steel glass washer" style="background:linear-gradient(160deg,#2a2a2a,#6e7274 55%,#3a3c3e)"><span class="mail"><svg width="11" height="8" viewBox="0 0 11 8"><rect width="11" height="8" rx="1" fill="#fff"/><path d="M0.5 .8l5 3.6 5-3.6" fill="none" stroke="#1d1d1d" stroke-width="1"/></svg></span><span class="tag">£10</span></div><h3>LOREM IPSUM IS SIMPLY DUMMY</h3><p>Contrary to popular belief, Lorem<br>Ipsum is not simply random text.<br>It has roots .</p><a class="more">VIEW DETAIL</a></article>
  <article class="card"><div class="shot" role="img" aria-label="Glass washer rack baskets" style="background:linear-gradient(160deg,#3a3a3a,#c8c8c8 55%,#4a4a4a)"><span class="mail"><svg width="11" height="8" viewBox="0 0 11 8"><rect width="11" height="8" rx="1" fill="#fff"/><path d="M0.5 .8l5 3.6 5-3.6" fill="none" stroke="#1d1d1d" stroke-width="1"/></svg></span><span class="tag">£20</span></div><h3>LOREM IPSUM IS SIMPLY DUMMY</h3><p>Contrary to popular belief, Lorem<br>Ipsum is not simply random text.<br>It has roots .</p><a class="more">VIEW DETAIL</a></article>
  <article class="card"><div class="shot" role="img" aria-label="Brass wall clock" style="background:radial-gradient(circle at 50% 45%,#d8c88a,#8a7040 40%,#1a1a1a 70%)"><span class="mail"><svg width="11" height="8" viewBox="0 0 11 8"><rect width="11" height="8" rx="1" fill="#fff"/><path d="M0.5 .8l5 3.6 5-3.6" fill="none" stroke="#1d1d1d" stroke-width="1"/></svg></span><span class="tag">£25</span></div><h3>LOREM IPSUM IS SIMPLY DUMMY</h3><p>Contrary to popular belief, Lorem<br>Ipsum is not simply random text.<br>It has roots .</p><a class="more">VIEW DETAIL</a></article>
  <article class="card"><div class="shot" role="img" aria-label="Wooden bedside lockers and mini fridge" style="background:linear-gradient(160deg,#2a2a2a,#9a5a2a 55%,#6a3a1a)"><span class="mail"><svg width="11" height="8" viewBox="0 0 11 8"><rect width="11" height="8" rx="1" fill="#fff"/><path d="M0.5 .8l5 3.6 5-3.6" fill="none" stroke="#1d1d1d" stroke-width="1"/></svg></span><span class="tag">£32</span></div><h3>LOREM IPSUM IS SIMPLY DUMMY</h3><p>Contrary to popular belief, Lorem<br>Ipsum is not simply random text.<br>It has roots .</p><a class="more">VIEW DETAIL</a></article>
</main>

<a class="show" href="#">SHOW MORE</a>

<footer class="foot">
  <h4 style="left:49px">Company Info</h4>
  <ul class="links"><li>Home</li><li>About us</li><li>Categories</li><li>Information</li><li>Contact Us</li></ul>
  <h4 style="left:254px">Contact Us</h4>
  <ul class="contact">
    <li><svg width="9" height="12" viewBox="0 0 9 12"><path d="M4.5 0a4.5 4.5 0 0 0-4.5 4.5C0 8 4.5 12 4.5 12S9 8 9 4.5A4.5 4.5 0 0 0 4.5 0z" fill="#fff"/><circle cx="4.5" cy="4.5" r="1.6" fill="#2d2d2d"/></svg>4470 Harrow Mill Road, Unit 12<br>Brookfield, CO 80511, USA</li>
    <li><svg width="11" height="11" viewBox="0 0 11 11"><path d="M2.2 0.5l2 2.4-1.2 1.4a7 7 0 0 0 3.7 3.7l1.4-1.2 2.4 2-1 1.7C4.6 10.2.8 6.4.5 1.5z" fill="#fff"/></svg>(555) 214-0736</li>
    <li><svg width="12" height="9" viewBox="0 0 11 8"><rect width="11" height="8" rx="1" fill="#fff"/><path d="M0.5 .8l5 3.6 5-3.6" fill="none" stroke="#2d2d2d" stroke-width="1"/></svg>hello@reclaimedtaverninnkit.com</li>
  </ul>
  <h4 style="left:579px">Newsletter Mailing List</h4>
  <div class="email-field"><svg width="12" height="9" viewBox="0 0 11 8"><rect x=".5" y=".5" width="10" height="7" fill="none" stroke="#fff"/><path d="M0.5 .8l5 3.6 5-3.6" fill="none" stroke="#fff"/></svg>E mail id</div>
  <a class="signup" href="#">SIGNUP</a>
  <div class="foot-brand"><span class="brand-mark"></span><span class="brand-name">Reclaimed Tavern &amp; Inn Kit</span></div>
  <div class="social"><i></i><i></i><i></i><i></i></div>
</footer>
<div class="base">© 2018 All Rights Reserved</div>

</body>
</html>
```